Orbin Vale Systems

Our company is about IT hardwares and IT solutions. IT hardware such as PC, RAMS, storage and servers. IT solutions such as project management, BA. We are also selling new technology too.

Target Market(s)

Consumer, Small to Medium Business, Corporate

Requirements
Must have
• The business card must have the following:
• Name:
• Title:
• Contact Number:
• Email address:
• Website:
• Color: Must match the logo color upgrade

```html
<!DOCTYPE html>
<html lang="en">
<head>
<meta charset="utf-8">
<title>Orbin Vale Systems — Business Card</title>
<link rel="stylesheet" href="https://fonts.googleapis.com/css2?family=Work+Sans:wght@400;500;600;700&display=swap">
<style>
  :root {
    --page-bg: #e4dfd8;
    --card-bg: #f3f0ec;
    --card-edge: #ddd6cd;
    --orange: #c97a34;
    --orange-deep: #b4602a;
    --slate: #545454;
    --ink: #3a3a3a;
    --muted: #5b5b5b;
  }
  * { margin: 0; padding: 0; box-sizing: border-box; }
  html, body {
    width: 1200px;
    height: 1047px;
    overflow: hidden;
    background: var(--page-bg);
    font-family: "Work Sans", sans-serif;
  }
  .business-card {
    position: absolute;
    left: 80px;
    top: 237px;
    width: 1040px;
    height: 573px;
    background: var(--card-bg);
    border: 1px solid var(--card-edge);
    border-radius: 26px;
    overflow: hidden;
    box-shadow: 0 18px 40px rgba(0,0,0,0.12);
  }
  .header-band {
    position: absolute;
    left: 0;
    top: 0;
    width: 100%;
    height: 190px;
    background: linear-gradient(90deg, var(--orange) 0%, var(--orange-deep) 100%);
  }
  .brand-name {
    position: absolute;
    left: 40px;
    top: 240px;
    font-size: 44px;
    font-weight: 700;
    letter-spacing: 0.5px;
    color: var(--slate);
    text-transform: uppercase;
    line-height: 1;
  }
  .holder {
    position: absolute;
    right: 40px;
    top: 318px;
    text-align: right;
  }
  .holder-name {
    font-size: 37px;
    font-weight: 500;
    color: var(--orange);
    text-transform: uppercase;
    line-height: 1;
  }
  .holder-title {
    margin-top: 10px;
    font-size: 24px;
    font-weight: 400;
    color: var(--ink);
  }
  .divider {
    position: absolute;
    left: 40px;
    right: 40px;
    top: 405px;
    height: 2px;
    background: var(--orange);
  }
  .contact-list {
    position: absolute;
    left: 40px;
    top: 446px;
    list-style: none;
  }
  .contact-item {
    display: flex;
    align-items: center;
    height: 33px;
    font-size: 24px;
    color: var(--muted);
  }
  .contact-icon {
    width: 16px;
    height: 16px;
    margin-right: 14px;
    fill: none;
    stroke: var(--orange);
    stroke-width: 2;
  }
  .address {
    position: absolute;
    right: 40px;
    top: 479px;
    text-align: right;
    font-style: normal;
    font-size: 24px;
    line-height: 33px;
    color: var(--ink);
  }
</style>
</head>
<body>
  <section class="business-card">
    <div class="header-band" role="img" aria-label="Decorative orange and grey header band"></div>

    <div class="brand-name">Orbin Vale Systems</div>

    <div class="holder">
      <div class="holder-name">Dorian Pell</div>
      <div class="holder-title">Director</div>
    </div>

    <div class="divider"></div>

    <ul class="contact-list">
      <li class="contact-item">
        <svg class="contact-icon" viewBox="0 0 16 16" aria-hidden="true">
          <path d="M3 2 L6 2 L7 5 L5 6.5 C6 9 7 10 9.5 11 L11 9 L14 10 L14 13 C8 14 2 8 3 2 Z"/>
        </svg>
        555-214-7730
      </li>
      <li class="contact-item">
        <svg class="contact-icon" viewBox="0 0 16 16" aria-hidden="true">
          <rect x="2" y="4" width="12" height="9"/>
          <path d="M2 4 L8 9 L14 4"/>
        </svg>
        info@orbinvale.com
      </li>
      <li class="contact-item">
        <svg class="contact-icon" viewBox="0 0 16 16" aria-hidden="true">
          <circle cx="8" cy="8" r="6"/>
          <path d="M2 8 H14 M8 2 C5 5 5 11 8 14 M8 2 C11 5 11 11 8 14"/>
        </svg>
        www.orbinvale.com
      </li>
    </ul>

    <address class="address">
      2280 Larkspur Mill Rd<br>
      Ashford, CA 95120-4418
    </address>
  </section>
</body>
</html>
```